New Massage Business needs a Card design

We need a card design for our new massage therapy business based in Sydney, Au. The business is getting a makeover, so a little later on we'll need shirts, various pamphlets and promotional flyers, and possibly a website. The winner will be offered those jobs as well.

Colour scheme should be green, black, and steel/charcoal grey. The business focuses on massage as an anatomical solution to stress, muscle aches, pains and fatigue. Ideally we'd like an anatomical image of the muscle system (ref to the attached files). In my mind this image takes up most of the left third of the card, and shows points of tension and pain at the neck and lower back. This image should be the grey portion of the card.

On the upper right is the other image attached, with a simple line drawing of a vehicle on the left end of the line, and a building on the right end replacing the stick figure (we have a therapist specializing in mobile massage). The blank part in the middle of the line should have "Vital Bodyworks", and in smaller writing below, "The Tension Fix".

Bottom right corner should have the contact and business details.
On the back we'd like a "next appointment" and "refer a friend" option.

If you have a design which doesn't fit the above, but you feel suits the business, please submit anyway - sometimes you don't know what you like until you see it.

Business Details:
Name: Vital Bodyworks - The Tension Fix

Massage Therapy

Business Details:
Contact name: Marcus
Title: Massage Therapist
Contact: 0458203167
Email: info@qlbrelief.example

Requirements
Must have
• Colour scheme should be green, black, and steel/charcoal grey. The business focuses on massage as an anatomical solution to stress, muscle aches, pains and fatigue. Ideally we'd like an anatomical image of the muscle system (ref to the attached files). In my mind this image takes up most of the left third of the card, and shows points of tension and pain at the neck and lower back. This image should be the grey portion of the card.
• On the upper right is the other image attached, with a simple line drawing of a vehicle on the left end of the line, and a building on the right end replacing the stick figure (we have a therapist specializing in mobile massage). The blank part in the middle of the line should have "Vital Bodyworks", and in smaller writing below, "The Tension Fix".
• Bottom right corner should have the contact and business details.
• On the back we'd like a "next appointment" and "refer a friend" option.
Nice to have
• Matt finish - no gloss
• If you have a design which doesn't fit the above, but you feel suits the business, please submit anyway - sometimes you don't know what you like until you see it.
Should not have
• Anything 'Zen'. The business promotes the physiological and scientific benefits of massage. For clients with spiritual or meditative needs, we refer out.

```html
<!DOCTYPE html>
<html lang="en">
<head>
<meta charset="utf-8">
<title>Vital Bodyworks – Business Card</title>
<link rel="stylesheet" href="https://fonts.googleapis.com/css2?family=Open+Sans:wght@400;600&display=swap">
<style>
  :root {
    --stage: #e4e2de;
    --paper: #ffffff;
    --ink: #111111;
    --green: #8cc23f;
    --panel-black: #141414;
    --muscle-dark: #b3271c;
    --muscle-light: #e2684f;
    --point: #d9d3e4;
    --point-ring: #a9c7d6;
  }
  * { margin: 0; padding: 0; box-sizing: border-box; }
  html, body { width: 1200px; height: 858px; overflow: hidden; }
  body {
    background: var(--stage);
    font-family: "Open Sans", Arial, sans-serif;
    color: var(--ink);
    display: flex;
    flex-direction: column;
    align-items: center;
    justify-content: center;
    gap: 30px;
  }
  .card {
    position: relative;
    width: 680px;
    height: 389px;
    background: var(--paper);
    box-shadow: 0 3px 10px rgba(0,0,0,.18);
    overflow: hidden;
  }
  .brand-name, .brand-tagline, .contact { white-space: nowrap; }

  /* Front */
  .title-band {
    position: absolute;
    left: 0; top: 34px;
    width: 385px; height: 92px;
    background: var(--green);
    padding: 10px 0 0 24px;
  }
  .brand-name { font-size: 40px; font-weight: 400; line-height: 1.1; }
  .brand-tagline { font-size: 24px; font-weight: 400; line-height: 1.1; padding-left: 56px; }
  .figure-panel {
    position: absolute;
    left: 0; top: 126px;
    width: 385px; height: 263px;
    background: var(--panel-black);
  }
  .figure-panel svg { display: block; }
  .contact {
    position: absolute;
    right: 26px; top: 118px;
    width: 255px;
    text-align: right;
  }
  .contact-name { font-size: 30px; font-weight: 600; line-height: 1.1; }
  .contact-title { font-size: 18px; line-height: 1.3; }
  .contact-line {
    font-size: 18px;
    line-height: 1.4;
    display: flex;
    align-items: center;
    justify-content: flex-end;
    gap: 8px;
  }
  .contact-phone { margin-top: 24px; }
  .contact-icon { width: 13px; height: 13px; flex: none; }

  /* Back */
  .back .figure-art { position: absolute; left: 40px; top: 120px; }
  .back .brand-block { position: absolute; left: 345px; top: 70px; }
  .back .brand-name { font-size: 40px; }
  .back .brand-tagline { font-size: 24px; padding-left: 8px; }
</style>
</head>
<body>

  <section class="card front" aria-label="Card front">
    <div class="title-band">
      <div class="brand-name">Vital Bodyworks</div>
      <div class="brand-tagline">The Tension Fix</div>
    </div>

    <div class="figure-panel">
      <svg width="385" height="263" viewBox="0 0 385 263">
        <defs>
          <linearGradient id="muscleFront" x1="0" y1="0" x2="1" y2="1">
            <stop offset="0" stop-color="var(--muscle-light)"/>
            <stop offset="1" stop-color="var(--muscle-dark)"/>
          </linearGradient>
        </defs>
        <rect class="figure-art" x="55" y="14" width="305" height="235" rx="40"
              fill="url(#muscleFront)" role="img"
              aria-label="Anatomical illustration of the human muscular system, seen from the back"/>
        <g class="tension-points" fill="var(--point)" stroke="var(--point-ring)" stroke-width="2">
          <circle cx="270" cy="70" r="20"/>
          <circle cx="100" cy="120" r="22"/>
          <circle cx="120" cy="200" r="20"/>
        </g>
      </svg>
    </div>

    <div class="contact">
      <div class="contact-name">Marcus</div>
      <div class="contact-title">Massage Therapist</div>
      <div class="contact-line contact-phone">0458203167
        <svg class="contact-icon" viewBox="0 0 14 14" aria-hidden="true">
          <rect width="14" height="14" fill="var(--ink)"/>
          <path d="M4 3.2l1.6 0 .7 2-1 .8a6 6 0 0 0 2.7 2.7l.8-1 2 .7 0 1.6c-4 .4-7.3-2.8-6.8-6.8z" fill="var(--paper)"/>
        </svg>
      </div>
      <div class="contact-line">info@qlbrelief.example
        <svg class="contact-icon" viewBox="0 0 14 14" aria-hidden="true">
          <rect width="14" height="14" fill="var(--ink)"/>
          <path d="M3 4.5h8v5H3z M3 4.5l4 3 4-3" fill="none" stroke="var(--paper)" stroke-width="1"/>
        </svg>
      </div>
    </div>
  </section>

  <section class="card back" aria-label="Card back">
    <svg class="figure-art" width="280" height="220" viewBox="0 0 280 220">
      <defs>
        <linearGradient id="muscleBack" x1="0" y1="0" x2="1" y2="1">
          <stop offset="0" stop-color="var(--muscle-light)"/>
          <stop offset="1" stop-color="var(--muscle-dark)"/>
        </linearGradient>
      </defs>
      <rect x="0" y="0" width="280" height="220" rx="40" fill="url(#muscleBack)" role="img"
            aria-label="Anatomical illustration of the human muscular system, seen from the back"/>
      <g class="tension-points" fill="var(--point)" stroke="var(--point-ring)" stroke-width="2">
        <circle cx="120" cy="30" r="16"/>
        <circle cx="210" cy="70" r="18"/>
        <circle cx="170" cy="170" r="17"/>
      </g>
    </svg>
    <div class="brand-block">
      <div class="brand-name">Vital Bodyworks</div>
      <div class="brand-tagline">The Tension Fix</div>
    </div>
  </section>

</body>
</html>
```